Business Card Design needed for letterhead design project

This project is linked to Letterhead Design For Corporate.

Our company needs a Business Card Design. Please refer to our original project in the link above.

Industry/Entity Type

Business

```html
<!DOCTYPE html>
<html lang="en">
<head>
<meta charset="utf-8">
<title>Veltra Energy — Stationery Set</title>
<link rel="stylesheet" href="https://fonts.googleapis.com/css2?family=Tinos:wght@400;700&display=swap">
<style>
  :root {
    --paper: #ffffff;
    --ink-deep: #0f4a2e;
    --brand-green: #1d5a1d;
    --brand-mid: #2d8a2d;
    --card-dark: #253a06;
    --card-stripe: #2c4309;
    --card-lime: #4fdc0a;
    --card-text: #3f9a1a;
    --accent-yellow: #e8e23a;
    --env-green: #138a05;
    --env-deep: #064a04;
    --env-stamp: #0f7a05;
    --env-ink: #0a3a0a;
    --env-brand: #0d5c0a;
    --ghost: #d8ebe2;
  }
  html, body {
    margin: 0;
    width: 1200px;
    height: 957px;
    overflow: hidden;
    background: var(--paper);
  }
  .canvas { display: block; width: 1200px; height: 957px; }
  text { font-family: "Tinos", "Times New Roman", serif; }
  .mark-name { fill: var(--ink-deep); font-weight: 700; font-size: 20px; letter-spacing: 1px; }
  .header-name { fill: var(--brand-green); font-size: 32px; }
  .header-address { fill: var(--brand-mid); font-size: 15px; }
  .card-bg { fill: var(--card-dark); }
  .card-lime { fill: var(--card-lime); }
  .card-rule { stroke: var(--card-lime); stroke-width: 1.5; fill: none; }
  .card-brand { fill: var(--card-text); font-size: 14px; }
  .card-brand .accent { fill: var(--accent-yellow); }
  .card-ghost { fill: #3b5420; font-size: 16px; font-weight: 700; letter-spacing: 1px; }
  .card-name { fill: var(--card-text); font-size: 22px; }
  .card-role { fill: var(--card-text); font-size: 6px; }
  .card-address { fill: var(--card-text); font-size: 9px; }
  .card-dots { fill: #3f6a14; }
  .env-bg { fill: var(--env-green); }
  .env-band { fill: var(--env-deep); }
  .env-stamp { fill: var(--env-stamp); }
  .env-address { fill: var(--env-ink); font-size: 24px; }
  .env-brand { fill: var(--env-brand); font-size: 28px; }
  .env-ghost { fill: #1a7a0e; font-size: 40px; font-weight: 700; letter-spacing: 2px; }
  .big-ghost { fill: var(--ghost); font-size: 64px; font-weight: 700; letter-spacing: 3px; }
  .strip-dark { fill: var(--env-deep); }
  .strip-cut { fill: var(--paper); }
</style>
</head>
<body>
<svg class="canvas" viewBox="0 0 1136 906" preserveAspectRatio="none" xmlns="http://www.w3.org/2000/svg">

  <!-- Letterhead header -->
  <g class="brand-header">
    <rect x="82" y="36" width="14" height="14" fill="var(--ink-deep)"/>
    <text class="mark-name" x="70" y="100">VELTRA</text>
    <text class="header-name" x="197" y="72">Veltra Energy</text>
    <text class="header-address" x="216" y="90">Address 1</text>
  </g>

  <!-- Business card front -->
  <g class="card-front" transform="translate(294,166) rotate(-17.6)">
    <rect class="card-bg" width="321" height="183"/>
    <path class="card-lime" d="M0 128 H321 V183 H0 Z"/>
    <path class="card-bg" d="M95 128 H321 V118 H270 L258 128 Z"/>
    <path class="card-bg" d="M95 122 H250 L262 132 H321 V128 H262 L250 150 H95 Q84 150 84 139 Q84 128 95 122 Z"/>
    <path class="card-bg" d="M96 124 H250 L262 134 H321 V122 H96 Z"/>
    <path class="card-bg" d="M96 124 H262 L272 132 H96 Q86 138 96 148 H250 L262 134 Z"/>
    <line class="card-rule" x1="170" y1="104" x2="321" y2="104"/>
    <text class="card-ghost" x="68" y="118">VELTRA</text>
    <text class="card-brand" x="98" y="143">Veltra <tspan class="accent">Energy</tspan></text>
  </g>

  <!-- Business card back -->
  <g class="card-back" transform="translate(700,214) rotate(-24.6)">
    <rect class="card-bg" width="319" height="181"/>
    <path class="card-lime" d="M0 140 H319 V181 H0 Z"/>
    <path class="card-bg" d="M0 140 H10 Q0 150 10 158 H110 L122 140 Z"/>
    <line class="card-rule" x1="118" y1="128" x2="319" y2="128"/>
    <text class="card-ghost" x="74" y="150" style="font-size:11px">VELTRA</text>
    <text class="card-name" x="22" y="48">Name</text>
    <text class="card-role" x="44" y="57">Designation</text>
    <g class="card-dots">
      <rect x="90" y="18" width="6" height="6"/><rect x="90" y="26" width="6" height="6"/>
      <rect x="90" y="34" width="6" height="6"/><rect x="90" y="42" width="6" height="6"/>
      <rect x="90" y="50" width="6" height="6"/><rect x="90" y="58" width="6" height="6"/>
      <rect x="90" y="66" width="6" height="6"/><rect x="90" y="74" width="6" height="6"/>
      <rect x="90" y="82" width="6" height="6"/>
    </g>
    <text class="card-address" x="108" y="28">Address 1</text>
    <text class="card-address" x="108" y="38">Address 1</text>
    <text class="card-address" x="108" y="48">Address 1</text>
    <text class="card-address" x="108" y="58">Address 1</text>
    <text class="card-brand" x="222" y="122">Veltra <tspan class="accent">Energy</tspan></text>
  </g>

  <!-- Envelope -->
  <g class="envelope" transform="translate(458,367) rotate(9)">
    <rect class="env-bg" width="659" height="335"/>
    <path class="env-band" d="M0 236 H659 V335 H0 Z"/>
    <path class="env-bg" d="M100 246 H659 V282 H470 L490 305 H659 V282 H100 Q80 282 80 264 Q80 246 100 246 Z"/>
    <path class="env-band" d="M100 280 H470 L488 302 H659 V294 H495 L478 280 Z" opacity="0"/>
    <line x1="150" y1="250" x2="659" y2="250" stroke="var(--env-deep)" stroke-width="2"/>
    <text class="env-ghost" x="100" y="205">VELTRA</text>
    <rect class="env-stamp" x="586" y="20" width="72" height="90"/>
    <text class="env-address" x="400" y="140">Address 1</text>
    <text class="env-address" x="400" y="168">Address 1</text>
    <text class="env-address" x="400" y="196">Address 1</text>
    <text class="env-brand" x="475" y="318">Veltra Energy</text>
  </g>

  <!-- Large faint brand name -->
  <text class="big-ghost" x="14" y="712">VELTRA</text>

  <!-- Letterhead footer strip -->
  <g class="footer-strip">
    <rect class="strip-dark" x="0" y="800" width="636" height="106"/>
    <path class="strip-cut" d="M636 805 H92 Q68 805 68 828 Q68 852 92 852 H430 L448 865 H636 Z"/>
  </g>
</svg>
</body>
</html>
```